Website redesign and new logo

Hi we feel that the colours, layout and style along with the logo which is only text at the moment is poor. It seems to lack a quality and luxurious feel and we are about selling high end curtains. The text logo is hard to read as well in my opinion. We are looking for a overall revamp and an new logo. We want to maintain the main parts of the home page but happy to consider any ideas that will improve web traffic. It does not really reflect our achievements either of having curtains recently featured on lumen 6 tv.
The website in question is www.velmorrahangings.co.uk

```html
<!DOCTYPE html>
<html lang="en">
<head>
<meta charset="utf-8">
<title>Velmorra Hangings</title>
<link href="https://fonts.googleapis.com/css2?family=Noto+Serif:wght@400;700&family=Arimo:wght@400;700&display=swap" rel="stylesheet">
<style>
:root{
  --purple:#8e1f6e;
  --orange:#ef9d3f;
  --footer:#e49a46;
  --ink:#2b2b2b;
  --text:#444;
  --rule:#e3d3dc;
  --tile:#333;
  --white:#fff;
}
*{box-sizing:border-box;margin:0;padding:0}
html,body{width:842px;height:1200px;overflow:hidden;background:var(--white)}
body{position:relative;font-family:"Arimo",Arial,sans-serif;color:var(--text);font-size:7.5px;line-height:1.55}
.abs{position:absolute}

/* header */
.brand{left:126px;top:30px;font-family:"Noto Serif",Georgia,serif;font-size:22px;line-height:1;color:var(--purple);letter-spacing:.5px;white-space:nowrap}
.tagline{left:592px;top:19px;font-family:"Noto Serif",Georgia,serif;font-size:10px;color:var(--purple);letter-spacing:.5px;white-space:nowrap}
.social{left:588px;top:40px;display:flex;gap:11px}
.social span{width:8px;height:8px;border-radius:50%;background:var(--purple)}

/* nav */
.nav{left:0;top:86px;width:842px;height:39px;border-top:1px solid var(--rule);border-bottom:1px solid var(--rule)}
.nav ul{list-style:none}
.nav li{position:absolute;top:15px;font-size:6.5px;line-height:1;font-weight:700;color:var(--purple);white-space:nowrap}
.nav li.active{color:var(--orange);font-weight:400}
.nav li.active::after{content:"";position:absolute;left:0;top:-16px;width:46px;border-top:1px solid var(--orange)}
.nav .sep{position:absolute;top:2px;width:1px;height:34px;background:var(--rule);transform:rotate(22deg)}

/* hero */
.hero{left:0;top:125px;width:842px;height:254px;background:linear-gradient(90deg,#c88a57 0%,#e0a677 28%,#d29464 48%,#b8834f 58%,#8fb7d6 66%,#a9cbe2 80%,#c58a5c 90%,#7d4f35 100%)}
.dots{left:128px;top:362px;display:flex;gap:4px}
.dots span{width:7px;height:7px;border-radius:50%;background:#b9d3e6;border:1px solid var(--white)}
.dots span:first-child{background:var(--white);border-color:#333}

/* features */
.feature{top:410px;width:190px}
.feature h3{font-family:"Noto Serif",Georgia,serif;font-weight:400;font-size:10px;color:var(--ink);line-height:1.25;display:flex;align-items:center;gap:6px}
.feature p{margin-top:14px}
.feature svg{flex:none}

/* welcome */
.section-title{font-family:"Noto Serif",Georgia,serif;font-weight:400;font-size:10px;color:var(--ink);letter-spacing:.2px}
.welcome{left:126px;top:536px;width:180px}
.welcome p{margin-top:12px}
.welcome a{display:block;margin-top:12px;color:var(--purple);font-weight:700;text-decoration:none}

.tile{width:186px;height:158px;background:var(--tile);border:1px solid #222;padding:3px}
.tile-media{height:110px}
.tile-caption{margin-top:3px;height:40px;border:1px solid #888;display:flex;flex-direction:column;justify-content:center;align-items:center;text-align:center;color:var(--white)}
.tile-caption strong{font-family:"Noto Serif",Georgia,serif;font-size:10.5px;line-height:1.25}
.tile-caption small{font-size:7px;color:#ddd}
.play{position:absolute;left:79px;top:49px;width:28px;height:22px;background:#222;display:flex;align-items:center;justify-content:center}

.divider{left:126px;top:720px;width:591px;border-top:1px solid #ddd}

/* areas */
.areas{left:126px;top:745px;width:190px}
.areas-media{position:absolute;left:0;top:27px;width:76px;height:70px;background:linear-gradient(90deg,#e9e9e6,#a9a9a6 30%,#f1f1ef 55%,#6e6e6c 80%,#e6e6e3)}
.areas ul{position:absolute;left:84px;top:23px;list-style:none}
.areas li{font-size:7.5px;line-height:17.5px;padding-left:13px;position:relative;white-space:nowrap}
.areas li::before{content:"\2735";position:absolute;left:0;color:#777;font-size:7px}

.promo{left:331px;top:746px;width:186px;height:158px;background:var(--tile);border:1px solid #222;padding:3px}
.promo-inner{height:100%;border:1px solid #777;display:flex;align-items:center;justify-content:center;text-align:center;font-family:"Noto Serif",Georgia,serif;font-weight:700;color:var(--white);font-size:13.5px;line-height:1.35;text-transform:uppercase}

.tips{left:531px;top:746px;width:186px;height:158px;background:var(--tile);border:1px solid #222;overflow:hidden}
.tips h4{font-family:"Noto Serif",Georgia,serif;font-size:11px;color:var(--white);text-align:center;margin-top:7px}
.tips .sub{text-align:center;color:#ddd;font-size:7px;letter-spacing:1px;line-height:1}
.tips .field{position:absolute;left:49px;width:83px;height:17px;background:#f3f3f3;font-size:7px;font-style:italic;color:#999;padding:3px 9px}
.tips-media{position:absolute;left:0;bottom:0;width:186px;height:68px;background:linear-gradient(160deg,#d8b84e,#9fc8d6 50%,#e7d38d);clip-path:polygon(100% 0,100% 100%,0 100%,0 75%)}

/* contact band */
.contact-band{left:0;top:942px;width:842px;height:54px;border-top:1px solid #e8c089;text-align:center;font-family:"Noto Serif",Georgia,serif;font-size:20px;color:var(--ink);line-height:56px}

/* footer */
.footer{left:0;top:996px;width:842px;height:204px;background:var(--footer);color:var(--white)}
.fcol{top:26px;width:130px}
.fcol h5{font-weight:400;font-size:8px;text-transform:uppercase;padding-bottom:5px;border-bottom:1px solid rgba(255,255,255,.6);font-family:"Noto Serif",Georgia,serif}
.fcol p{margin-top:14px;font-size:7.2px}
.fcol ul{list-style:none;margin-top:13px}
.fcol li{font-size:7.2px;line-height:15.5px;display:flex;align-items:center;gap:6px;white-space:nowrap}
.fcol .dark{color:#3a2a1a}
.addr li{align-items:flex-start;margin-bottom:9px;line-height:1.55;white-space:normal}
.footer-rule{left:126px;top:167px;width:591px;border-top:1px solid rgba(255,255,255,.6)}
.copyright{left:126px;top:178px;font-size:7px}
</style>
</head>
<body>

<header>
  <div class="brand abs">Velmorra Hangings</div>
  <div class="tagline abs">We Love Design</div>
  <div class="social abs" aria-label="Social links"><span></span><span></span><span></span><span></span><span></span></div>
</header>

<nav class="nav abs">
  <ul>
    <li class="active" style="left:126px">HOME</li>
    <li style="left:178px">ABOUT US</li>
    <li style="left:247px">NEWS</li>
    <li style="left:301px">FABRICS</li>
    <li style="left:366px">SCATTER CUSHIONS &amp; BED THROWS</li>
    <li style="left:524px">GALLERY</li>
    <li style="left:588px">TESTIMONIALS</li>
    <li style="left:673px">CONTACT US</li>
  </ul>
  <span class="sep" style="left:164px"></span>
  <span class="sep" style="left:232px"></span>
  <span class="sep" style="left:286px"></span>
  <span class="sep" style="left:346px"></span>
  <span class="sep" style="left:508px"></span>
  <span class="sep" style="left:572px"></span>
  <span class="sep" style="left:658px"></span>
</nav>

<div class="hero abs" role="img" aria-label="Elegant living room with cream sofa, gilded mirror and full-length curtains beside a sea-view balcony"></div>
<div class="dots abs"><span></span><span></span><span></span><span></span></div>

<section class="feature abs" style="left:128px">
  <h3><svg width="30" height="27" viewBox="0 0 30 27"><rect x="1" y="1" width="28" height="3" fill="#333"/><path d="M3 4 Q8 14 5 26 H11 Q9 14 13 4Z M27 4 Q22 14 25 26 H19 Q21 14 17 4Z" fill="#333"/></svg><span style="text-align:center">Curtain Fabric types<br>include</span></h3>
  <p style="padding-left:37px">An expert in-home measuring services and professional hanging.</p>
</section>
<section class="feature abs" style="left:333px">
  <h3><svg width="32" height="27" viewBox="0 0 32 27"><rect x="5" y="1" width="26" height="25" rx="2" fill="none" stroke="#333" stroke-width="2.5"/><rect x="1" y="8" width="5" height="18" rx="2" fill="none" stroke="#333" stroke-width="2"/><rect x="9" y="5" width="18" height="5" fill="#333"/><rect x="9" y="13" width="8" height="9" fill="#333"/><path d="M20 14h7M20 18h7M20 22h7" stroke="#333" stroke-width="2"/></svg><span style="text-align:center">Our Latest Curtain and<br>Fabric News</span></h3>
  <p style="padding-left:36px">We provide a made to curtain services</p>
</section>
<section class="feature abs" style="left:537px">
  <h3><svg width="31" height="27" viewBox="0 0 31 27"><circle cx="10" cy="7" r="5.5" fill="#333"/><path d="M0 27 Q0 14 10 14 Q20 14 20 27Z" fill="#333"/><circle cx="21" cy="8" r="4.5" fill="#333"/><path d="M19 15 Q30 13 31 27 H22Z" fill="#333"/></svg><span>Our Customers love us</span></h3>
  <p style="padding-left:36px">My room is so much warmer now I have curtains that properly fit, and the thermal lining really does seem to make a difference</p>
</section>

<section class="welcome abs">
  <h2 class="section-title">Welcome to Velmorra Hangings</h2>
  <p>Hi my name is Maren. Velmorra Hangings is my inspiration. I'm passionate about my fabrics and take pride in what I do. I've always enjoyed creating the WOW factor. Designer curtains have never looked so good!</p>
  <a href="#">View the Portfolio</a>
</section>

<article class="tile abs" style="left:331px;top:536px">
  <div class="tile-media" role="img" aria-label="Close-up of gold and navy scatter cushions on a bed throw" style="background:linear-gradient(135deg,#2f3a45,#6d7f86 40%,#c9b53c 65%,#e8e2c8)"></div>
  <div class="tile-caption"><strong>Scatter Cushions and<br>Bed Throws</strong></div>
</article>
<article class="tile abs" style="left:531px;top:536px">
  <div class="tile-media" role="img" aria-label="Video still of patterned brown and cream curtains at a window" style="position:relative;background:linear-gradient(90deg,#e8dccb,#8a6a52 25%,#f2ece2 50%,#7e5f48 75%,#e6dac7)">
    <span class="play"><svg width="10" height="11" viewBox="0 0 10 11"><path d="M0 0L10 5.5L0 11Z" fill="#fff"/></svg></span>
  </div>
  <div class="tile-caption"><strong>Meet Integrity designer</strong><small>Decorative tips: Curtains</small></div>
</article>

<div class="divider abs"></div>

<section class="areas abs">
  <h2 class="section-title">The areas we cover include</h2>
  <div class="areas-media" role="img" aria-label="Black and white patterned curtains framing a bright window"></div>
  <ul>
    <li>Curtains Berkshire</li><li>Curtains Buckinghamshire</li><li>Curtains Oxfordshire</li><li>Curtains Winchester</li><li>Curtains Guildford</li><li>Curtains Oxford</li>
  </ul>
</section>

<aside class="promo abs"><div class="promo-inner">See our<br>curtains on<br>lumen 6,<br><br>double your<br>house for half a<br>money</div></aside>

<aside class="tips abs">
  <h4>Free Curtain Tips</h4>
  <div class="sub">Maren Designer Curtains</div>
  <div class="field" style="top:45px">NAME:</div>
  <div class="field" style="top:69px">PHONE:</div>
  <div class="field" style="top:94px">EMAIL:</div>
  <div class="tips-media" role="img" aria-label="Fan of patterned fabric swatches in yellow, blue and grey"></div>
</aside>

<div class="contact-band abs">Contact us, Click Right Here !</div>

<footer class="footer abs">
  <div class="fcol abs" style="left:126px">
    <h5>More about Velmorra</h5>
    <p>Velmorra Hangings is a young and exciting company full of innovative ideas. This is built on years of experience and expertise. We are passionate about what we do, and take genuine pleasure ... <span class="dark">Read More</span></p>
  </div>
  <div class="fcol abs" style="left:279px">
    <h5>Most liked posts</h5>
    <ul>
      <li>&#9829; Nice Gallery Post (70)</li>
      <li>&#9829; Ohhh Sweeeeet...... (37)</li>
      <li>&#9829; Catwalk (25)</li>
      <li>&#9829; R.T. Halden (1901-1960) (7)</li>
      <li>&#9829; Video Showcase Post (4)</li>
    </ul>
  </div>
  <div class="fcol abs" style="left:432px">
    <h5>Recent tweets</h5>
    <p style="padding-left:14px">Lorem ipsum dolor sit amet, consetetur sadipscing elitr, sed diam nonumy eirmod tempor invidunt ut labore et dolore magna aliquyam erat, sed diam <span class="dark">about 15days ago</span></p>
  </div>
  <div class="fcol abs addr" style="left:586px">
    <h5>Our address</h5>
    <ul>
      <li><svg width="9" height="9" viewBox="0 0 9 9"><path d="M4.5 0L9 4H7.5V9H5.5V6H3.5V9H1.5V4H0Z" fill="#fff"/></svg><span>12 Harrow Lane, Elmsworth, Westshire, EL4 2QT</span></li>
      <li><svg width="9" height="8" viewBox="0 0 9 8"><rect x="0" y="0" width="9" height="8" rx="1" fill="#fff"/><rect x="2" y="2" width="5" height="1.5" fill="#e49a46"/></svg><span>0300 555 0182</span></li>
      <li><svg width="9" height="8" viewBox="0 0 9 8"><rect x="2" y="0" width="5" height="3" fill="#fff"/><rect x="0" y="3" width="9" height="5" rx="1" fill="#fff"/></svg><span>(305) 555-0199</span></li>
      <li><svg width="9" height="7" viewBox="0 0 9 7"><rect width="9" height="7" fill="#fff"/><path d="M0 0L4.5 4L9 0" stroke="#e49a46" fill="none"/></svg><span>info@velmorrahangings.co.uk</span></li>
    </ul>
  </div>
  <div class="footer-rule abs"></div>
  <div class="copyright abs">Copyrights Velmorra Hangings All Rights Reserved</div>
</footer>

</body>
</html>
```